IT Network Consultancy - Business Card

kelbrin systems is a IT network consultancy based in London. We're looking for a smart, modern and professional business card design. Our website is here: www.kelbrinsystems.co.uk

Key things that should be included on the card (with examples):

Company Logo
Name
Position / Job Title: Network Consultant
Mobile Phone Number: +44 (0) 7700 900418
Land Line: +44 (0) 1632 960735
Email Address: name@kelbrinsystems.co.uk
Web Site URL: www.kelbrinsystems.co.uk

Target Market(s)

Large enterprise / global companies / corporates

Industry/Entity Type

Business

Requirements
Must have
• Incorporate our logo - which is attached to the project. They are in AI format (can be opened in Inkscape).

The design should be double sided and fit on a UK standard 85mm × 55mm card and be in a format that retains the quality when printed.
Nice to have
• The project does not have to conform to the colour of our website but this should give you inspiration of the style we like.
Should not have
• Bright colours. Pictures are not necessary.

```html
<!DOCTYPE html>
<html lang="en">
<head>
<meta charset="utf-8">
<title>Kelbrin Systems – Business Card</title>
<link href="https://fonts.googleapis.com/css2?family=Montserrat:wght@300;500;600;700&display=swap" rel="stylesheet">
<style>
  :root {
    --page: #f9fbfc;
    --slate: #8fb0b8;
    --brand-blue: #3592d6;
    --deep-blue: #2a7fc4;
    --pale-blue: #5aa8e0;
    --white: #ffffff;
    --caption: #3a8fd2;
  }
  * { margin: 0; padding: 0; box-sizing: border-box; }
  html, body { width: 1200px; height: 400px; overflow: hidden; background: var(--page); }
  body { position: relative; font-family: "Montserrat", sans-serif; }

  .card {
    position: absolute; top: 48px; width: 525px; height: 301px;
    border-radius: 20px; overflow: hidden;
  }
  .card-front { left: 64px; background: var(--slate); }
  .card-back { left: 611px; background: var(--brand-blue); }

  .front-photo { position: absolute; inset: 0; }

  .wordmark {
    position: absolute; display: flex; align-items: center; gap: 14px;
    color: var(--white); font-weight: 300; letter-spacing: 1px; white-space: nowrap;
  }
  .wordmark-dot { width: 38px; height: 38px; border-radius: 50%; background: var(--brand-blue); flex: none; }
  .card-front .wordmark { left: 146px; top: 54px; font-size: 27px; }

  .holder { position: absolute; left: 166px; top: 172px; }
  .holder-name { color: var(--brand-blue); font-weight: 700; font-size: 17px; letter-spacing: .5px; }
  .holder-role { color: var(--white); font-weight: 600; font-size: 10px; margin: 2px 0 0 68px; letter-spacing: .3px; }
  .holder-role::before { content: "•"; color: var(--brand-blue); margin-right: 5px; }

  .contacts { position: absolute; left: 230px; top: 214px; border-collapse: collapse; }
  .contacts th {
    color: var(--deep-blue); font-weight: 500; font-size: 7px; letter-spacing: .5px;
    text-align: right; padding: 0 6px 0 0; height: 13.5px;
  }
  .contacts th::after { content: " •"; color: var(--white); margin-left: 3px; }
  .contacts td { color: var(--white); font-weight: 600; font-size: 10.5px; letter-spacing: .3px; }

  .back-photo { position: absolute; inset: 0; }
  .back-band { position: absolute; left: 0; right: 0; top: 102px; height: 84px; background: var(--slate); }
  .card-back .wordmark { left: 50%; top: 144px; transform: translate(-50%, -50%); font-size: 30px; }
  .back-url {
    position: absolute; left: 0; right: 0; top: 191px; text-align: center;
    color: var(--white); font-weight: 700; font-size: 11px; letter-spacing: 3px;
  }

  .side-label {
    position: absolute; top: 355px; color: var(--caption); font-weight: 700; font-size: 14px; letter-spacing: .5px;
  }
  .label-front { left: 471px; }
  .label-divider { left: 587px; font-style: normal; }
  .label-back { left: 687px; }
</style>
</head>
<body>

<section class="card card-front">
  <svg class="front-photo" width="525" height="301" viewBox="0 0 525 301" role="img" aria-label="Photograph of network cabling in blue tones">
    <defs>
      <linearGradient id="front-photo-tone" x1="0" y1="0" x2="1" y2="1">
        <stop offset="0" stop-color="#2f86c9"/>
        <stop offset="0.5" stop-color="#5aa8e0"/>
        <stop offset="1" stop-color="#3592d6"/>
      </linearGradient>
    </defs>
    <path d="M0 0 H110 V150 L190 301 H0 Z" fill="url(#front-photo-tone)"/>
  </svg>

  <div class="wordmark"><span class="wordmark-dot"></span>KELBRIN SYSTEMS</div>

  <div class="holder">
    <p class="holder-name">FIRST, LASTNAME</p>
    <p class="holder-role">NETWORK CONSULTANT</p>
  </div>

  <table class="contacts">
    <tr><th>MOBILE</th><td>+44 (0) 7700 900418</td></tr>
    <tr><th>LANDLINE</th><td>+44 (0) 1632 960735</td></tr>
    <tr><th>EMAIL</th><td>NAME@KELBRINSYSTEMS.CO.UK</td></tr>
    <tr><th>WEBSITE</th><td>KELBRINSYSTEMS.CO.UK</td></tr>
  </table>
</section>

<section class="card card-back">
  <svg class="back-photo" width="525" height="301" viewBox="0 0 525 301" role="img" aria-label="Faint photograph of patch cables in blue">
    <defs>
      <linearGradient id="back-photo-tone" x1="0" y1="0" x2="1" y2="0">
        <stop offset="0" stop-color="#3592d6"/>
        <stop offset="0.6" stop-color="#3592d6"/>
        <stop offset="1" stop-color="#4a9edb"/>
      </linearGradient>
    </defs>
    <rect width="525" height="301" fill="url(#back-photo-tone)"/>
  </svg>
  <div class="back-band"></div>
  <div class="wordmark"><span class="wordmark-dot"></span>KELBRIN SYSTEMS</div>
  <p class="back-url">WWW.KELBRINSYSTEMS.CO.UK</p>
</section>

<span class="side-label label-front">FRONT</span>
<span class="side-label label-divider">//</span>
<span class="side-label label-back">BACK</span>

</body>
</html>
```